Mabikay spice shop needs a web design

We need a web design former new company based in sydney australia. Called 'Mabikay, spice shop'.
We produce caribbean/west indies product alcohol, spirits, condiments, candies, preserved food, jams, pates.
We would like to see a design that reflect the caribbean without being tacky.
We want modern, high level design as we do high level products.
Updates

Reason: There is a lot of good proposition but I need a few more days to mature my decision. Thanks for your hard work Jorel

Industry/Entity Type

Hospitality

Number of Pages Required

1 page

Font styles to use
Decorative
Script

Requirements
Must have
• The logo, the name of the business

```html
<!DOCTYPE html>
<html lang="en">
<head>
<meta charset="utf-8">
<title>Mabikay spice shop</title>
<link href="https://fonts.googleapis.com/css2?family=Roboto:wght@300;400;500&family=Roboto+Condensed:wght@400;700&display=swap" rel="stylesheet">
<style>
:root{
  --cream:#f1dba6;
  --cream-light:#fbf1d8;
  --gold:#c9a634;
  --gold-dark:#a88a25;
  --navy:#232c5c;
  --ink:#2b2b2b;
  --body:#555;
  --accent:#d27a2e;
  --white:#fff;
  --foot:rgba(255,255,255,.85);
}
*{margin:0;padding:0;box-sizing:border-box}
html,body{width:734px;height:1200px;overflow:hidden}
body{position:relative;font-family:"Roboto",Arial,sans-serif;color:var(--ink);
  background:radial-gradient(ellipse at 50% 0%,var(--cream-light) 0%,#f6e6bd 35%,var(--cream) 70%);}
.abs{position:absolute}
.deco-left{left:0;top:270px;width:60px;height:250px;background:linear-gradient(160deg,rgba(40,130,150,.55) 0%,rgba(236,120,30,.8) 55%,rgba(245,190,80,.4) 100%);border-radius:0 60px 60px 0;opacity:.8}
.deco-right{left:674px;top:210px;width:60px;height:250px;background:linear-gradient(200deg,rgba(140,80,20,.6) 0%,rgba(200,140,50,.5) 60%,rgba(240,200,100,.2) 100%);border-radius:60px 0 0 60px}
.search{left:60px;top:47px;width:130px;height:21px;border:1px solid #333;border-radius:3px;font-size:7px;color:#444;padding:5px 9px;background:rgba(255,255,255,.3)}
.search svg{position:absolute;right:8px;top:6px}
.question{right:91px;top:44px;text-align:right;font-size:10px;line-height:13px;color:var(--ink)}
.phone-ring{left:650px;top:46px;width:22px;height:22px;border:1px solid #333;border-radius:50%;display:flex;align-items:center;justify-content:center}
.ribbon{left:18px;top:107px;width:682px;height:38px}
.nav{left:52px;top:104px;width:630px;height:34px;background:var(--gold);display:flex;align-items:center;font-size:7.8px;color:var(--white);letter-spacing:.2px}
.nav a{position:absolute;color:var(--white);text-decoration:none}
.logo{left:313px;top:27px;width:106px;height:106px;border-radius:50%;background:var(--white);border:2px solid var(--gold);box-shadow:0 0 0 4px rgba(255,255,255,.6);display:flex;align-items:center;justify-content:center;font-family:"Roboto Condensed",sans-serif;font-size:21px;color:var(--navy)}
.panel{left:60px;top:140px;width:614px;height:848px;background:var(--white);border-radius:0 0 14px 14px;box-shadow:0 1px 3px rgba(0,0,0,.15)}
.panel-shadow{left:140px;top:986px;width:454px;height:18px;background:radial-gradient(ellipse at 50% 0%,rgba(90,60,10,.45) 0%,rgba(90,60,10,0) 70%)}
.hero{left:64px;top:143px;width:605px;height:290px;background:linear-gradient(120deg,#4a3b2d 0%,#7a4a26 30%,#a8452a 45%,#5b4a38 65%,#3d3630 100%)}
.hero-title{left:455px;top:298px;font-family:"Roboto Condensed",sans-serif;font-weight:700;font-size:32px;line-height:29px;color:var(--white);text-shadow:0 1px 3px rgba(0,0,0,.5)}
.hero-sub{left:456px;top:362px;font-size:7.5px;line-height:11px;color:var(--white)}
.slider-tab{left:307px;top:414px;width:120px;height:20px}
.dots{left:345px;top:425px;display:flex;gap:5px;align-items:center}
.dots span{width:6px;height:6px;border-radius:50%;background:#444}
.dots .on{width:10px;height:10px;border:1px solid var(--gold);background:radial-gradient(circle,var(--gold) 45%,#fff 50%)}
.welcome{left:60px;top:460px;width:614px;text-align:center;font-family:"Roboto Condensed",sans-serif;font-size:22.5px;color:var(--ink)}
.welcome em{font-style:normal;color:var(--navy)}
.intro{left:105px;top:498px;width:524px;text-align:center;font-size:7.2px;line-height:12.5px;color:var(--body)}
.rule{left:180px;top:550px;width:374px;height:6px;background:radial-gradient(ellipse at 50% 0%,rgba(0,0,0,.08),rgba(0,0,0,0) 70%)}
.section-title{left:60px;top:582px;width:614px;text-align:center;font-size:19px;font-weight:300;color:var(--ink)}
.card{width:135px;height:161px;top:617px;border:1px solid #e6e6e6;background:var(--white);text-align:center}
.card .photo{margin:5px;height:103px}
.card h3{font-size:9.5px;font-weight:400;margin-top:10px;color:var(--ink)}
.card p{font-size:6.5px;line-height:11.5px;color:var(--body);margin-top:3px}
.news-title{left:76px;top:815px;font-size:12.5px;color:var(--ink)}
.arrows{left:625px;top:815px;display:flex;gap:3px}
.arrows span{width:14px;height:14px;border:1px solid #888;border-radius:50%;display:flex;align-items:center;justify-content:center}
.news-line{left:76px;top:843px;width:582px;height:1px;background:#e8e8e8}
.thumb{width:82px;height:82px;border-radius:50%;border:3px solid var(--white);box-shadow:0 0 0 1px #ddd}
.news h4{font-size:10px;font-weight:400;color:var(--ink)}
.news .date{font-size:8.5px;color:var(--accent);margin-top:9px}
.news p{font-size:6.6px;line-height:12.3px;color:var(--body);margin-top:6px;width:165px}
.news .more{font-size:6.8px;color:var(--ink);margin-top:7px}
.foot-h{top:1026px;font-size:10.5px;color:var(--foot);letter-spacing:.2px}
.map{left:60px;top:1052px;width:170px;height:86px;border:2px solid rgba(255,255,255,.8);background:linear-gradient(135deg,#dfe3da,#cfd8cc 50%,#e6e2d6)}
.social li,.links li{list-style:none;font-size:8px;color:var(--foot);display:flex;align-items:center;height:22px}
.social .ic{width:15px;height:15px;border:1px solid var(--foot);border-radius:50%;margin-right:7px}
.contact{left:393px;top:1050px;font-size:7.5px;line-height:12px;color:var(--foot)}
.links li{height:18px;font-size:7px}
.links li::before{content:"";border-left:3px solid var(--foot);border-top:2.5px solid transparent;border-bottom:2.5px solid transparent;margin-right:8px}
.foot-line{left:60px;top:1162px;width:614px;height:1px;background:rgba(255,255,255,.4)}
.copy{left:0;top:1173px;width:734px;text-align:center;font-size:7px;color:var(--foot)}
</style>
</head>
<body>
<div class="abs deco-left" role="img" aria-label="Colourful Caribbean wave decoration"></div>
<div class="abs deco-right" role="img" aria-label="Palm tree and paint splash decoration"></div>

<header>
  <div class="abs search">Search
    <svg width="8" height="8" viewBox="0 0 8 8"><circle cx="3.2" cy="3.2" r="2.4" fill="none" stroke="#222" stroke-width="1.2"/><line x1="5" y1="5" x2="7.5" y2="7.5" stroke="#222" stroke-width="1.3"/></svg>
  </div>
  <div class="abs question">Have any Question?<br>+1 555 0142 7731</div>
  <div class="abs phone-ring">
    <svg width="10" height="10" viewBox="0 0 10 10"><path d="M2 1l2 2-1 1.2c.6 1.3 1.5 2.2 2.8 2.8L7 6l2 2-1.3 1.3C4.5 9 1 5.5.7 2.3z" fill="#222"/></svg>
  </div>
  <svg class="abs ribbon" viewBox="0 0 682 38">
    <polygon points="0,6 40,0 40,34 0,38 12,22" fill="var(--gold-dark)"/>
    <polygon points="682,6 642,0 642,34 682,38 670,22" fill="var(--gold-dark)"/>
  </svg>
  <nav class="abs nav">
    <a style="left:35px">HOME</a>
    <a style="left:83px">ABOUT MABIKAY</a>
    <a style="left:181px">OUR PRODUCT</a>
    <a style="left:389px">SPICE SHOP</a>
    <a style="left:465px">REVIEWS</a>
    <a style="left:525px">CONTACT US</a>
  </nav>
  <div class="abs logo">Mabikay</div>
</header>

<main>
  <div class="abs panel"></div>
  <div class="abs hero" role="img" aria-label="Wooden spoons of colourful spices on a rustic table"></div>
  <div class="abs hero-title">MABIKAY<br>SPICE SHOP</div>
  <div class="abs hero-sub">Lorem ipsum dolor sit amet, consectetur adipiscing elit,<br>sed do eiusmod tempor incididunt ut labore et</div>
  <svg class="abs slider-tab" viewBox="0 0 120 20"><path d="M0 20C25 20 30 0 60 0S95 20 120 20Z" fill="#fff"/></svg>
  <div class="abs dots"><span class="on"></span><span></span><span></span><span></span></div>

  <h1 class="abs welcome">Welcome To <em>Mabikay, spice shop</em></h1>
  <p class="abs intro">Lorem ipsum dolor sit amet, consectetur adipiscing elit, sed do eiusmod tempor incididunt ut labore et dolore magna aliqua. Ut enim ad minim veniam, quis nostrud exercitation ullamco laboris nisi ut aliquip ex ea commodo consequat. Duis aute irure dolor in reprehenderit in voluptate velit esse cillum dolore eu fugiat nulla pariatur. Excepteur sint occaecat cupidatat non proident, sunt in culpa qui officia</p>
  <div class="abs rule"></div>

  <h2 class="abs section-title">Our Product</h2>
  <article class="abs card" style="left:77px"><div class="photo" role="img" aria-label="Wine glasses with grapes and cheese" style="background:linear-gradient(135deg,#6b5a3a,#8a2a2a 50%,#c9a45a)"></div><h3>ALCOHOL</h3><p>Lorem ipsum dolor sit amet, consec<br>teer adipiscing. Prsent</p></article>
  <article class="abs card" style="left:225px"><div class="photo" role="img" aria-label="Jar of strawberry jam with fresh strawberries" style="background:linear-gradient(135deg,#b8302a,#d9453a 45%,#4f7a2e)"></div><h3>JAMS</h3><p>Lorem ipsum dolor sit amet, consec<br>teer adipiscing. Prsent</p></article>
  <article class="abs card" style="left:374px"><div class="photo" role="img" aria-label="Red wine being poured into a glass" style="background:linear-gradient(135deg,#f3e9dc,#c9a98a 50%,#8a1f22)"></div><h3>SPIRITS</h3><p>Lorem ipsum dolor sit amet, consec<br>teer adipiscing. Prsent</p></article>
  <article class="abs card" style="left:522px"><div class="photo" role="img" aria-label="Jar of preserved apples beside fresh apples" style="background:linear-gradient(135deg,#8a8a80,#c7492e 50%,#d83a26)"></div><h3>PRESERVED FOOD</h3><p>Lorem ipsum dolor sit amet, consec<br>teer adipiscing. Prsent</p></article>

  <h2 class="abs news-title">LATEST NEWS</h2>
  <div class="abs arrows">
    <span><svg width="5" height="6" viewBox="0 0 5 6"><path d="M4 0L1 3l3 3" fill="none" stroke="#666"/></svg></span>
    <span><svg width="5" height="6" viewBox="0 0 5 6"><path d="M1 0l3 3-3 3" fill="none" stroke="#666"/></svg></span>
  </div>
  <div class="abs news-line"></div>

  <div class="abs thumb" style="left:79px;top:865px;background:radial-gradient(circle,#e84a8a,#f2c24a 40%,#3a8a4a 75%)" role="img" aria-label="Swirled lollipop and candies"></div>
  <article class="abs news" style="left:180px;top:863px">
    <h4>Nulla at diam ornare, aliquam urna</h4>
    <div class="date">JULY 25, 2015</div>
    <p>Nulla at diam ornare, aliquam urna vel, commodo urna. Nam id risus a est luctus consectetur quis eget libero. Suspendisse potenti.</p>
    <div class="more">READ MORE +</div>
  </article>
  <div class="abs thumb" style="left:399px;top:865px;background:radial-gradient(circle,#d98a2a,#7a3a14 60%,#3a2214)" role="img" aria-label="Glass decanter of amber rum"></div>
  <article class="abs news" style="left:499px;top:863px">
    <h4>Nulla at diam ornare, aliquam urna</h4>
    <div class="date">JULY 25, 2015</div>
    <p>Nulla at diam ornare, aliquam urna vel, commodo urna. Nam id risus a est luctus consectetur quis eget libero. Suspendisse potenti.</p>
    <div class="more">READ MORE +</div>
  </article>
  <div class="abs panel-shadow"></div>
</main>

<footer>
  <h3 class="abs foot-h" style="left:60px;font-weight:400">OUR LOCATION</h3>
  <div class="abs map" role="img" aria-label="Street map of the shop location"></div>

  <h3 class="abs foot-h" style="left:272px;font-weight:400">SOCIAL MEDIA</h3>
  <ul class="abs social" style="left:272px;top:1049px">
    <li><span class="ic"></span>Friendwall</li>
    <li><span class="ic"></span>Chirper</li>
    <li><span class="ic"></span>Circlenet</li>
    <li><span class="ic"></span>Viewtube</li>
  </ul>

  <h3 class="abs foot-h" style="left:393px;font-weight:400">CONTACT US</h3>
  <div class="abs contact">18 Harbour Lane #12,<br>Marrow Bay 4021</div>
  <svg class="abs" style="left:395px;top:1081px" width="11" height="11" viewBox="0 0 10 10"><path d="M2 1l2 2-1 1.2c.6 1.3 1.5 2.2 2.8 2.8L7 6l2 2-1.3 1.3C4.5 9 1 5.5.7 2.3z" fill="none" stroke="rgba(255,255,255,.85)" stroke-width=".8"/></svg>
  <div class="abs contact" style="left:416px;top:1082px">Call Us 555-014-2290<br>555-014-2290</div>
  <svg class="abs" style="left:395px;top:1115px" width="12" height="9" viewBox="0 0 12 9"><rect x=".5" y=".5" width="11" height="8" fill="none" stroke="rgba(255,255,255,.85)"/><path d="M.5 .5L6 5l5.5-4.5" fill="none" stroke="rgba(255,255,255,.85)"/></svg>
  <div class="abs contact" style="left:416px;top:1114px">hello@mabikayspice.com</div>

  <h3 class="abs foot-h" style="left:587px;font-weight:400">QUICK LINKS</h3>
  <ul class="abs links" style="left:588px;top:1051px">
    <li>ALCOHOL</li><li>SPIRITS</li><li>CONDIMENTS</li><li>CANDIES</li><li>PRESERVED FOOD</li>
  </ul>

  <div class="abs foot-line"></div>
  <div class="abs copy">2015 © Copyrights Mabikay, spice shop</div>
</footer>
</body>
</html>
```